Plumbing Van Vehicle Signage

I need a design for vehicle signage for a group of plumbing vans. The company name is 'Kestrel Gas & Plumbing'. I do all types of plumbing and gas fitting but specialise in general maintenance plumbing and gas fitting.

Industry/Entity Type

Plumbing

Requirements
Must have
• Must be eye catching. Must be able to go on a white back ground as the vans are white. Must contain phone number

```html
<!DOCTYPE html>
<html lang="en">
<head>
<meta charset="utf-8">
<title>Kestrel Gas &amp; Plumbing – Van Signage</title>
<link rel="stylesheet" href="https://fonts.googleapis.com/css2?family=Montserrat:wght@700;800&display=swap">
<style>
  :root {
    --page-bg: #ededed;
    --wrap-blue: #3f78c4;
    --wrap-blue-deep: #2d5aa8;
    --wrap-yellow: #f6c35a;
    --wrap-orange: #ef9a3a;
    --wrap-orange-deep: #e06f35;
    --panel-white: #ffffff;
    --ink-blue: #2f5fb3;
  }
  html, body {
    margin: 0;
    width: 1200px;
    height: 1200px;
    overflow: hidden;
    background: radial-gradient(ellipse at 50% 40%, #f7f7f7 0%, var(--page-bg) 70%);
  }
  .van-side-artwork {
    position: absolute;
    left: 100px;
    top: 390px;
    width: 1000px;
    height: 400px;
  }
  .brand-name {
    font-family: "Montserrat", sans-serif;
    font-weight: 800;
    fill: var(--ink-blue);
  }
  .phone-number {
    font-family: "Montserrat", sans-serif;
    font-weight: 800;
    fill: var(--ink-blue);
    letter-spacing: 1px;
  }
</style>
</head>
<body>
  <svg class="van-side-artwork" viewBox="0 0 1000 400" xmlns="http://www.w3.org/2000/svg" aria-label="Kestrel Gas &amp; Plumbing van side wrap">
    <defs>
      <linearGradient id="blueField" x1="0" y1="0" x2="0" y2="1">
        <stop offset="0" stop-color="var(--wrap-blue)"/>
        <stop offset="1" stop-color="var(--wrap-blue-deep)"/>
      </linearGradient>
      <linearGradient id="orangeField" x1="0" y1="0" x2="0" y2="1">
        <stop offset="0" stop-color="var(--wrap-yellow)"/>
        <stop offset="0.5" stop-color="var(--wrap-orange)"/>
        <stop offset="1" stop-color="var(--wrap-orange-deep)"/>
      </linearGradient>
    </defs>

    <g class="wrap-fields">
      <rect class="field-orange" x="0" y="0" width="1000" height="400" rx="24" fill="url(#orangeField)"/>
      <path class="field-blue" d="M24 0 H640 L440 400 H24 A24 24 0 0 1 0 376 V24 A24 24 0 0 1 24 0 Z" fill="url(#blueField)"/>
      <polygon class="field-white-band" points="605,70 1000,70 1000,200 540,200" fill="var(--panel-white)"/>
    </g>

    <g class="brand-lockup">
      <circle class="brand-dot" cx="660" cy="135" r="26" fill="var(--wrap-orange)"/>
      <text class="brand-name" x="700" y="140" font-size="50">KESTREL</text>
      <text class="brand-name" x="702" y="172" font-size="20" letter-spacing="2">GAS &amp; PLUMBING</text>
    </g>

    <text class="phone-number" x="755" y="260" font-size="38" text-anchor="middle">0400 555 182</text>
  </svg>
</body>
</html>
```